Debt Relief Landing Page Design

I need a landing page designed (and the accompanying Thank You page) for my client.

I have drafted the wireframes for the layout of the pages (attached) and need a professional looking finish.

The main colours to use are green and blue as per their current branding, see website for specifications - http://www.clearpathledger.com.au/

Industry/Entity Type

Debt

Coding

Coded - Design and coding required

```html
<!DOCTYPE html>
<html lang="en">
<head>
<meta charset="utf-8">
<title>Clear Path Ledger – Debt Consolidation</title>
<link rel="stylesheet" href="https://fonts.googleapis.com/css2?family=Lato:ital,wght@0,400;0,700;1,400&display=swap">
<style>
:root{
  --green:#5e8c2b;
  --green-dark:#4f7822;
  --navy:#2d4f7e;
  --navy-text:#1f3d6b;
  --ink:#222;
  --paper:#fff;
  --footer:#dcdcdc;
  --sun:#f1e3c6;
  --sun-ring:#e9dcc2;
}
*{box-sizing:border-box;margin:0;padding:0}
html,body{width:698px;height:1200px;overflow:hidden;background:var(--paper)}
body{position:relative;font-family:"Lato",Arial,sans-serif;color:var(--ink)}
.abs{position:absolute}

.site-header{left:0;top:0;width:698px;height:68px;box-shadow:0 2px 4px rgba(0,0,0,.18);background:#fff}
.brand{left:48px;top:20px;font-size:22px;font-weight:700;color:var(--navy-text);letter-spacing:-.3px;display:flex;align-items:center;gap:7px}
.brand-mark{width:12px;height:12px;background:var(--green);border-radius:50%}
.contact{right:46px;top:15px;text-align:right;font-size:15px;color:var(--navy-text);line-height:1.25}
.contact strong{display:block;color:var(--green);font-weight:400}

.hero-title{left:47px;top:92px;font-size:22px;font-weight:700;color:var(--green)}
.hero-sub{left:77px;top:135px;font-size:14px;font-weight:700;color:var(--navy-text);line-height:1.3}
.hero-copy{left:47px;top:186px;width:372px;font-size:9.2px;line-height:1.35}
.hero-copy p{margin-bottom:14px}

.consult{left:444px;top:86px;width:209px;height:273px;background:var(--navy);border-radius:3px;color:#fff;padding:8px 8px 0}
.consult h2{text-align:center;font-size:14px;font-weight:700}
.consult .lead{text-align:center;font-size:7.5px;font-weight:700;line-height:1.3;margin-top:2px;padding-bottom:4px;border-bottom:1px solid #fff}
.field{display:flex;justify-content:space-between;align-items:flex-start;margin-top:8px;height:18px}
.field label{font-size:8.6px;width:62px;line-height:1.2}
.field span{width:135px;height:18px;background:#fff;border:1px solid #ccc;border-radius:2px;color:#777;font-size:8px;padding:3px 3px;font-family:Arial,sans-serif}
.field.tall{height:26px;margin-top:8px}
.consult .cta{display:block;margin:18px auto 0;width:156px}

.cta{background:var(--green);color:#fff;font-size:10.5px;text-align:center;height:28px;line-height:28px;border-radius:2px;box-shadow:1px 2px 3px rgba(0,0,0,.35)}
.cta.wide{width:183px;left:258px}

.section-bar{left:47px;top:382px;width:605px;height:24px;background:var(--navy);color:#fff;font-size:12px;font-weight:700;padding:4px 4px}

.service{width:140px;text-align:left}
.service .icon{display:block;margin:0 auto;width:34px;height:34px}
.service h3{text-align:center;font-size:10px;font-weight:700;margin-top:11px}
.service p{font-size:6.6px;line-height:1.4;margin-top:10px;padding-left:4px}

.rule{left:47px;top:738px;width:605px;height:1px;background:#aaa}
.clients-title{left:0;width:698px;top:773px;text-align:center;font-size:14px;font-weight:700;color:var(--green)}

.quote{width:164px;height:132px;background:var(--navy);border-radius:4px;color:#fff;padding:9px 8px 0;font-size:7.6px;font-style:italic;line-height:1.42}
.quote q{quotes:none}
.quote q::before,.quote q::after{content:"\201C";color:#d84a3a;font-weight:700;margin-right:2px}
.quote q::after{content:"\201D";margin:0 0 0 2px}
.quote cite{display:block;text-align:right;color:var(--green);font-size:6.6px;margin-top:6px}

.site-footer{left:0;top:1175px;width:698px;height:25px;background:var(--footer);font-size:6.8px;padding:8px 35px;display:flex;justify-content:space-between}
.site-footer a{color:#2b5fa8;text-decoration:none}
</style>
</head>
<body>

<header class="site-header abs">
  <div class="brand abs"><i class="brand-mark"></i>Clear Path Ledger</div>
  <div class="contact abs">Contact us on:<strong>1300418262</strong></div>
</header>

<h1 class="hero-title abs">Looking To Consolidate Your Debt?</h1>
<h2 class="hero-sub abs">If You Have Over $10,000 In Debt, We Can<br>Help You To Be Debt Free In 3-5 Years.</h2>
<div class="hero-copy abs">
  <p>Ledger Advisers is Australia’s debt help relief Specialists. Through years of industry experience and knowledge, our team of debt management experts can actively advise you on how to get out of the red, fast.</p>
  <p>At Ledger Advisers we are able to actively rectify your debt problems by creating simple and affordable payment plans for all debts.</p>
  <p>To get a free, no obligation consultation by one of our industry leading experts, as well as a Debt Management Plan simply fill out the form on the right and we will be in contact with you within 48 hours.</p>
</div>

<form class="consult abs">
  <h2>Free Consultation</h2>
  <p class="lead">Fill In The Form Below To Receive Your Free, No Obligation Consultation</p>
  <div class="field"><label>Name</label><span>Enter your Name</span></div>
  <div class="field"><label>Phone</label><span>Enter your Phone No.</span></div>
  <div class="field"><label>Email</label><span>Enter your Post Email</span></div>
  <div class="field"><label>Post Code</label><span>Enter your Post Code</span></div>
  <div class="field tall"><label>Unsecured Debt</label><span>Enter your Unsecured Debt</span></div>
  <div class="field tall"><label>Preferred Call Time</label><span>Enter Preferred Call Time</span></div>
  <div class="cta">Get My Free Consultation</div>
</form>

<div class="section-bar abs">Some Of Our Debt Relief Services</div>

<div class="service abs" style="left:79px;top:424px">
  <svg class="icon" role="img" aria-label="Umbrella service icon" viewBox="0 0 34 34"><circle cx="17" cy="17" r="16" fill="var(--sun)" stroke="var(--sun-ring)" stroke-width="2"/></svg>
  <h3>Debt Consolidation Loans</h3>
  <p>Stop getting hassled by creditors. Let us consolidate your personal into an easy repayment plans.</p>
</div>
<div class="service abs" style="left:281px;top:424px">
  <svg class="icon" role="img" aria-label="Umbrella service icon" viewBox="0 0 34 34"><circle cx="17" cy="17" r="16" fill="var(--sun)" stroke="var(--sun-ring)" stroke-width="2"/></svg>
  <h3>Mortgage Refinance</h3>
  <p>Consolidate your debt into available home equity, significantly reducing your general repayments.</p>
</div>
<div class="service abs" style="left:483px;top:424px">
  <svg class="icon" role="img" aria-label="Umbrella service icon" viewBox="0 0 34 34"><circle cx="17" cy="17" r="16" fill="var(--sun)" stroke="var(--sun-ring)" stroke-width="2"/></svg>
  <h3>Debt Agreements</h3>
  <p>A viable alternative to bankruptcy and debt consolidation loans.</p>
</div>
<div class="service abs" style="left:79px;top:553px">
  <svg class="icon" role="img" aria-label="Umbrella service icon" viewBox="0 0 34 34"><circle cx="17" cy="17" r="16" fill="var(--sun)" stroke="var(--sun-ring)" stroke-width="2"/></svg>
  <h3>Credit Repair</h3>
  <p>Assist you in removing unfair, disputable and incorrect information from your credit file / information, which you believe should not be there.</p>
</div>
<div class="service abs" style="left:281px;top:553px">
  <svg class="icon" role="img" aria-label="Umbrella service icon" viewBox="0 0 34 34"><circle cx="17" cy="17" r="16" fill="var(--sun)" stroke="var(--sun-ring)" stroke-width="2"/></svg>
  <h3>Bankruptcy</h3>
  <p>We will work with you to accurately determine of bankruptcy is the sole option.</p>
</div>
<div class="service abs" style="left:483px;top:553px">
  <svg class="icon" role="img" aria-label="Umbrella service icon" viewBox="0 0 34 34"><circle cx="17" cy="17" r="16" fill="var(--sun)" stroke="var(--sun-ring)" stroke-width="2"/></svg>
  <h3>Bad Credit Loans</h3>
  <p>We work in your best interests to provide a consolidation loan that turns your bad credit history into a positive financial situation.</p>
</div>

<div class="cta wide abs" style="top:691px">Get My Free Consultation</div>

<div class="rule abs"></div>
<h2 class="clients-title abs">What Clients Say</h2>

<blockquote class="quote abs" style="left:65px;top:813px"><q>We were on the verge of losing our car and did not know what to do, but now we are in a affordable arrangement to catch up our car payments and are on our way to debt free future. We are even thinking of buying a house, without your help this would not be possible</q><cite>Marlene, Box Hill, VIC</cite></blockquote>
<blockquote class="quote abs" style="left:265px;top:813px"><q>I am very relived and can now get my life on track. I very sincerely appreciate all of your assistance. You treated me like a person and never condemned me for the situation I was in. If ever I have the opportunity to recommend your services, I will sincerely recommend you. Take care and thank thank you.</q><cite>Priya, Howlong, NSW</cite></blockquote>
<blockquote class="quote abs" style="left:465px;top:813px"><q>I had lost my job and my creditors were about to take legal action against me. I had no idea of what options I had and thought I was going to lose everything I had worked so hard for, with your help I was able to work out a payment arrangement that everyone I owed money to accepted. I would not have known what to do without your help</q><cite>Owen, Penrith, NSW</cite></blockquote>
<blockquote class="quote abs" style="left:65px;top:966px"><q>I am writing this letter to express my appreciation for all your help with sorting my finances out. My consultant worked through an easy to understand payment plan which I can easily afford and understand. Thank you.</q><cite>Keith, Liverpool, NSW</cite></blockquote>
<blockquote class="quote abs" style="left:265px;top:966px"><q>The previous finance company I went to couldn’t consolidate all my debt so put me in worse position. Ledger Advisers stepped in, I am now making only one payment saves me $500 per month.</q><cite>Rafael, Doonside, NSW</cite></blockquote>
<blockquote class="quote abs" style="left:465px;top:966px"><q>Thank you so much for you helping me so quick with my finances. All the credit agencies have stop calling and can live a normal life hassle free.</q><cite>Tessa, Hoppers, VIC</cite></blockquote>

<div class="cta wide abs" style="top:1124px">Get My Free Consultation</div>

<footer class="site-footer abs">
  <span>© 2000 to 2015 - All rights reserved. <a href="#">Terms and Conditions</a></span>
  <span><a href="#">Home</a> | <a href="#">About</a></span>
</footer>

</body>
</html>
```